Providing Back Office Solutions to Financial Advisors and Attorney Needs a Business Card Design

Need a Business Card Design that speaks to Financial Advisor and Attorneys. Some of the word that come to mind is Clean/Simple & Futuristic.

Industry/Entity Type

Business

```html
<!DOCTYPE html>
<html lang="en">
<head>
<meta charset="utf-8">
<title>Nexora Back Office Solutions – Business Card</title>
<link rel="stylesheet" href="https://fonts.googleapis.com/css2?family=Open+Sans:wght@400;600&display=swap">
<style>
  :root {
    --bg: #2b2b2d;
    --blue-light: #0a8fd3;
    --blue-mid: #0878bd;
    --blue-dark: #0a5a98;
    --ink-blue: #0d5fae;
    --rule-blue: #1d6fb8;
    --white: #ffffff;
    --shadow: rgba(0,0,0,0.45);
  }
  * { margin: 0; padding: 0; box-sizing: border-box; }
  html, body {
    width: 1200px; height: 880px; overflow: hidden;
    background: var(--bg);
    font-family: "Open Sans", Arial, sans-serif;
  }
  .stage { position: relative; width: 1200px; height: 880px; }

  .card {
    position: absolute;
    width: 600px; height: 340px;
    border-radius: 22px;
    box-shadow: 0 18px 40px var(--shadow);
    overflow: hidden;
  }

  /* Front */
  .card-front {
    left: 60px; top: 80px;
    background: radial-gradient(ellipse at 70% 20%, var(--blue-light), var(--blue-mid) 55%, var(--blue-dark));
    color: var(--white);
  }
  .card-front .lockup {
    position: absolute; left: 0; right: 0; top: 110px;
    display: flex; justify-content: center; align-items: center; gap: 16px;
  }
  .mark-square {
    width: 46px; height: 46px; background: var(--white);
  }
  .brand-name {
    font-weight: 400; font-size: 54px; letter-spacing: 3px; line-height: 1;
  }
  .tagline {
    font-size: 13px; letter-spacing: 1px; margin-top: 6px;
  }
  .card-front .tagline { color: var(--white); }
  .card-front .web {
    position: absolute; left: 0; right: 0; top: 238px;
    text-align: center; font-size: 15px; letter-spacing: 9px;
  }

  /* Back */
  .card-back {
    left: 540px; top: 470px;
    background: var(--white);
    color: var(--ink-blue);
  }
  .card-back .lockup {
    position: absolute; left: 46px; top: 120px;
    display: flex; align-items: center; gap: 16px;
  }
  .card-back .mark-square { background: var(--ink-blue); }
  .card-back .brand-name { color: var(--ink-blue); font-size: 50px; }
  .card-back .tagline { color: var(--ink-blue); }
  .person {
    position: absolute; right: 44px; top: 34px; text-align: right;
  }
  .person-name { font-weight: 600; font-size: 19px; letter-spacing: 0.5px; }
  .person-role { font-size: 13px; margin-top: -2px; }

  .contact-rule {
    position: absolute; left: 36px; right: 36px; top: 256px;
    height: 1.5px; background: var(--rule-blue);
  }
  .contacts {
    position: absolute; left: 40px; right: 36px; top: 268px;
    display: flex; align-items: center; gap: 16px;
    font-size: 13.5px; line-height: 1.45;
  }
  .contact-group { display: flex; flex-direction: column; }
  .contact-line { display: flex; align-items: center; gap: 6px; }
  .divider { width: 1.5px; height: 40px; background: var(--rule-blue); }
  .icon { width: 14px; height: 14px; flex: none; }
</style>
</head>
<body>
<main class="stage">

  <section class="card card-front" aria-label="Card front">
    <div class="lockup">
      <div class="mark-square"></div>
      <div>
        <div class="brand-name">NEXORA</div>
        <div class="tagline">BACK OFFICE SOLUTIONS</div>
      </div>
    </div>
    <div class="web">www.nexoraoffice.com</div>
  </section>

  <section class="card card-back" aria-label="Card back">
    <div class="person">
      <div class="person-name">DANIEL REEVE</div>
      <div class="person-role">Owner</div>
    </div>

    <div class="lockup">
      <div class="mark-square"></div>
      <div>
        <div class="brand-name">NEXORA</div>
        <div class="tagline">BACK OFFICE SOLUTIONS</div>
      </div>
    </div>

    <div class="contact-rule"></div>

    <div class="contacts">
      <div class="contact-group">
        <div class="contact-line">
          <svg class="icon" viewBox="0 0 14 14"><circle cx="7" cy="7" r="6.3" fill="none" stroke="currentColor" stroke-width="1.2"/><rect x="5" y="3.5" width="4" height="7" rx="0.8" fill="none" stroke="currentColor"/></svg>
          <span>(01) 5550 1427</span>
        </div>
        <div class="contact-line">
          <svg class="icon" viewBox="0 0 14 14"><circle cx="7" cy="7" r="6.3" fill="currentColor"/><rect x="3.8" y="5" width="6.4" height="4.5" rx="0.8" fill="#fff"/></svg>
          <span>(01) 5550 1428</span>
        </div>
      </div>
      <div class="divider"></div>
      <div class="contact-group">
        <div class="contact-line">
          <svg class="icon" viewBox="0 0 14 14"><circle cx="7" cy="7" r="6.3" fill="currentColor"/><rect x="3.5" y="4.5" width="7" height="5" fill="#fff"/><path d="M3.5 4.5 L7 7.5 L10.5 4.5" fill="none" stroke="currentColor" stroke-width="0.9"/></svg>
          <span>info@nexoraoffice.com</span>
        </div>
        <div class="contact-line">
          <svg class="icon" viewBox="0 0 14 14"><circle cx="7" cy="7" r="6.3" fill="currentColor"/><circle cx="7" cy="7" r="3.6" fill="none" stroke="#fff" stroke-width="0.9"/><path d="M3.4 7 H10.6 M7 3.4 V10.6" stroke="#fff" stroke-width="0.9"/></svg>
          <span>www.nexoraoffice.com</span>
        </div>
      </div>
      <div class="divider"></div>
      <div class="contact-group">
        <span>PO BOX 456 Kent Road</span>
        <span>3rd street Adelaide</span>
      </div>
    </div>
  </section>

</main>
</body>
</html>
```